Party Decoration Set Designs - Rose Gold theme - more example images just added

We are looking for a set of designs for a set of party decorations. It’s a Rose Gold colored theme. I have attached some photos of some glittery rose gold items that I think would go good with the theme. There are also some photos of full sets of decorations in other colors schemes to give an idea of what we are looking for.

We would like to have designs for the items below:

1- Happy Birthday Flag Banner- looking for something unique. Size- 5”X7” WXL

2- hanging swirl cards ( photo examples attached) 4”X6” approx. can be different sizes and shapes.

3- centerpiece designs- photo examples attached. Middle
Piece that’s says Happy Birthday should be 5”X 7” and the smaller surrounding pieces 3X5

4 - round candy stickers and candy wrappers. Examples below. .75 inch

The photos below are of products currently sold. We would like to be very similar to these but just a little different to make our own. And then to have a Happy Birthday banner created to match the theme.

Some of these example photos below are from different themes and colors But I included them because they are the complete set we want to create. First we will do a generic “Happy Birthday” Set with rose gold glitter theme and then later we will add the Sweet 16 birthday theme as well and 40th, 50th etc.

On the centerpieces where the example photos how a large “40”, we would like this to be a larger “Happy Birthday” design. Then surrounded by some smaller designs.
I look forward to receiving your ideas

Target Market(s)

Anyone looking for birthday Peru decorations for a female.

Font styles to use
Other font styles liked:
• Open to designer suggestion

Requirements
Must have
• Happy Birthday Banner, Hanging swirl cards, centerpiece cards, cake topper
Nice to have
• We are certainly open to any creative ideas.
Should not have
• I just now added some example images of a very good set of exactly what we want but its in a different theme. This is a black gold set and our requested design is more feminine and Rose Gold color

```html
<!DOCTYPE html>
<html lang="en">
<head>
<meta charset="utf-8">
<title>Rose Glitter Birthday Banner and Hanging Swirl Cards</title>
<link href="https://fonts.googleapis.com/css2?family=Michroma&family=Titan+One&display=swap" rel="stylesheet">
<style>
  :root {
    --paper: #ffffff;
    --blush: #f6c8d4;
    --glitter: #e0468c;
    --glitter-deep: #c2185b;
    --berry: #b5174f;
    --ink: #000000;
  }
  html, body {
    margin: 0;
    padding: 0;
    width: 1200px;
    height: 773px;
    overflow: hidden;
    background: var(--paper);
  }
  .sheet {
    position: relative;
    width: 1200px;
    height: 773px;
  }
  .section-label {
    position: absolute;
    margin: 0;
    font-family: "Michroma", sans-serif;
    font-size: 19px;
    font-weight: 400;
    color: var(--ink);
    letter-spacing: 0.5px;
    white-space: nowrap;
  }
  .section-label--banner { left: 477px; top: 24px; }
  .section-label--cards { left: 157px; top: 626px; }
  .flag {
    position: absolute;
    width: 115px;
    height: 160px;
  }
  .flag-letter {
    font-family: "Titan One", sans-serif;
    font-size: 112px;
    fill: var(--ink);
    text-anchor: middle;
  }
  .swirl-card {
    position: absolute;
  }
</style>
</head>
<body>
<main class="sheet">
  <svg width="0" height="0" style="position:absolute" aria-hidden="true">
    <defs>
      <clipPath id="flag-clip">
        <polygon points="0,0 115,0 115,160 57.5,141 0,160"/>
      </clipPath>
      <pattern id="glitter-stripes" patternUnits="userSpaceOnUse" width="40" height="32" patternTransform="rotate(-14)">
        <rect width="40" height="32" fill="var(--blush)"/>
        <rect y="6" width="40" height="20" fill="var(--glitter)"/>
      </pattern>
      <linearGradient id="crown-tone" x1="0" y1="0" x2="0" y2="1">
        <stop offset="0" stop-color="#f2a6c2"/>
        <stop offset="1" stop-color="#f6c8d4"/>
      </linearGradient>
      <linearGradient id="card-glitter" x1="0" y1="0" x2="1" y2="1">
        <stop offset="0" stop-color="#e85a98"/>
        <stop offset="1" stop-color="#d63a80"/>
      </linearGradient>
    </defs>
  </svg>

  <h1 class="section-label section-label--banner">BANNER DESIGN</h1>

  <!-- Row one: HAPPY -->
  <svg class="flag flag--framed" style="left:108px;top:78px" viewBox="0 0 115 160">
    <polygon points="0,0 115,0 115,160 57.5,141 0,160" fill="var(--blush)"/>
    <polygon points="7,7 108,7 108,152 57.5,135 7,152" fill="var(--blush)" stroke="var(--glitter)" stroke-width="5"/>
    <rect x="16" y="22" width="83" height="104" rx="6" fill="url(#crown-tone)" role="img" aria-label="Glitter crown ornament"/>
  </svg>
  <svg class="flag flag--striped" style="left:259px;top:78px" viewBox="0 0 115 160">
    <rect width="115" height="160" fill="url(#glitter-stripes)" clip-path="url(#flag-clip)"/>
    <text class="flag-letter" x="57.5" y="113">H</text>
  </svg>
  <svg class="flag flag--framed" style="left:402px;top:78px" viewBox="0 0 115 160">
    <polygon points="0,0 115,0 115,160 57.5,141 0,160" fill="var(--blush)"/>
    <polygon points="7,7 108,7 108,152 57.5,135 7,152" fill="var(--blush)" stroke="var(--glitter)" stroke-width="5"/>
    <text class="flag-letter" x="57.5" y="113">A</text>
  </svg>
  <svg class="flag flag--striped" style="left:545px;top:78px" viewBox="0 0 115 160">
    <rect width="115" height="160" fill="url(#glitter-stripes)" clip-path="url(#flag-clip)"/>
    <text class="flag-letter" x="57.5" y="113">P</text>
  </svg>
  <svg class="flag flag--framed" style="left:688px;top:78px" viewBox="0 0 115 160">
    <polygon points="0,0 115,0 115,160 57.5,141 0,160" fill="var(--blush)"/>
    <polygon points="7,7 108,7 108,152 57.5,135 7,152" fill="var(--blush)" stroke="var(--glitter)" stroke-width="5"/>
    <text class="flag-letter" x="57.5" y="113">P</text>
  </svg>
  <svg class="flag flag--striped" style="left:831px;top:78px" viewBox="0 0 115 160">
    <rect width="115" height="160" fill="url(#glitter-stripes)" clip-path="url(#flag-clip)"/>
    <text class="flag-letter" x="57.5" y="113">Y</text>
  </svg>
  <svg class="flag flag--framed" style="left:974px;top:78px" viewBox="0 0 115 160">
    <polygon points="0,0 115,0 115,160 57.5,141 0,160" fill="var(--blush)"/>
    <polygon points="7,7 108,7 108,152 57.5,135 7,152" fill="var(--blush)" stroke="var(--glitter)" stroke-width="5"/>
    <rect x="16" y="22" width="83" height="104" rx="6" fill="url(#crown-tone)" role="img" aria-label="Glitter crown ornament"/>
  </svg>

  <!-- Row two: BIRTHDAY -->
  <svg class="flag flag--striped" style="left:81px;top:306px" viewBox="0 0 115 160">
    <rect width="115" height="160" fill="url(#glitter-stripes)" clip-path="url(#flag-clip)"/>
    <text class="flag-letter" x="57.5" y="113">B</text>
  </svg>
  <svg class="flag flag--framed" style="left:211px;top:306px" viewBox="0 0 115 160">
    <polygon points="0,0 115,0 115,160 57.5,141 0,160" fill="var(--blush)"/>
    <polygon points="7,7 108,7 108,152 57.5,135 7,152" fill="var(--blush)" stroke="var(--glitter)" stroke-width="5"/>
    <text class="flag-letter" x="57.5" y="113">I</text>
  </svg>
  <svg class="flag flag--striped" style="left:344px;top:306px" viewBox="0 0 115 160">
    <rect width="115" height="160" fill="url(#glitter-stripes)" clip-path="url(#flag-clip)"/>
    <text class="flag-letter" x="57.5" y="113">R</text>
  </svg>
  <svg class="flag flag--framed" style="left:474px;top:306px" viewBox="0 0 115 160">
    <polygon points="0,0 115,0 115,160 57.5,141 0,160" fill="var(--blush)"/>
    <polygon points="7,7 108,7 108,152 57.5,135 7,152" fill="var(--blush)" stroke="var(--glitter)" stroke-width="5"/>
    <text class="flag-letter" x="57.5" y="113">T</text>
  </svg>
  <svg class="flag flag--striped" style="left:607px;top:306px" viewBox="0 0 115 160">
    <rect width="115" height="160" fill="url(#glitter-stripes)" clip-path="url(#flag-clip)"/>
    <text class="flag-letter" x="57.5" y="113">H</text>
  </svg>
  <svg class="flag flag--framed" style="left:737px;top:306px" viewBox="0 0 115 160">
    <polygon points="0,0 115,0 115,160 57.5,141 0,160" fill="var(--blush)"/>
    <polygon points="7,7 108,7 108,152 57.5,135 7,152" fill="var(--blush)" stroke="var(--glitter)" stroke-width="5"/>
    <text class="flag-letter" x="57.5" y="113">D</text>
  </svg>
  <svg class="flag flag--striped" style="left:870px;top:306px" viewBox="0 0 115 160">
    <rect width="115" height="160" fill="url(#glitter-stripes)" clip-path="url(#flag-clip)"/>
    <text class="flag-letter" x="57.5" y="113">A</text>
  </svg>
  <svg class="flag flag--framed" style="left:1000px;top:306px" viewBox="0 0 115 160">
    <polygon points="0,0 115,0 115,160 57.5,141 0,160" fill="var(--blush)"/>
    <polygon points="7,7 108,7 108,152 57.5,135 7,152" fill="var(--blush)" stroke="var(--glitter)" stroke-width="5"/>
    <text class="flag-letter" x="57.5" y="113">Y</text>
  </svg>

  <h2 class="section-label section-label--cards">HANGING SWIRL CARDS</h2>

  <!-- Hanging swirl cards -->
  <svg class="swirl-card swirl-card--crown" style="left:495px;top:584px" width="122" height="105" viewBox="0 0 122 105">
    <path d="M4,10 Q10,2 18,12 L30,28 Q40,20 46,12 Q50,2 60,2 Q70,2 74,12 Q80,20 90,28 L104,12 Q112,2 118,10 L100,100 Q99,104 94,104 L28,104 Q23,104 22,100 Z" fill="var(--blush)"/>
    <path d="M11,16 L30,38 Q44,30 50,18 Q54,9 60,9 Q66,9 70,18 Q76,30 90,38 L111,16 L95,97 L27,97 Z" fill="url(#card-glitter)" role="img" aria-label="Glitter crown card with hand-lettered Birthday party"/>
  </svg>
  <svg class="swirl-card swirl-card--hexagon" style="left:634px;top:577px" width="119" height="123" viewBox="0 0 119 123">
    <polygon points="59.5,2 117,32 117,91 59.5,121 2,91 2,32" fill="var(--blush)" stroke="var(--blush)" stroke-width="4" stroke-linejoin="round"/>
    <polygon points="59.5,10 109,36 109,87 59.5,113 10,87 10,36" fill="var(--ink)" role="img" aria-label="Hexagon card with hand-lettered Let's Celebrate and glitter candles"/>
  </svg>
  <svg class="swirl-card swirl-card--round" style="left:780px;top:586px" width="108" height="108" viewBox="0 0 108 108">
    <circle cx="54" cy="54" r="53" fill="var(--berry)"/>
    <circle cx="54" cy="54" r="47" fill="var(--ink)" role="img" aria-label="Round card with hand-lettered Happy Birthday to you in pink glitter"/>
    <circle cx="54" cy="54" r="40" fill="none" stroke="var(--glitter)" stroke-width="2"/>
  </svg>
</main>
</body>
</html>
```